Medical Software Informational Flyer and Website Design

Our company, Copper Vale Systems, is launching a new product, the Vale Clinic Flow Platform. It is a software suite that will increase the productivity and volume of a LASIK practice.

We want this flyer to be a companion to our big reveal presentation at OPX and NVCSE; it's primary purpose is to inform potential clients on the many ways this software will help their practice. It is also obviously a promotional material. Because it is a companion to our presentation, we feel that it is acceptable for the flyer to contain much more text than would normally be reasonable in a flyer; it will go into more detail about the 12 major selling points of our software than our presentation time will allow. Having said that, however, we still want there to be "breathing room" for the design and the viewer's eyes.

We have uploaded our logo, both in full color and in white with no background (often used for watermarks, but certainly not restricted for that use alone). Our logo should be accompanied by either "Copper Vale Systems" or "VCF" using the Trajan Pro font (unoriginal, we know, but it's what we've chosen). We have included a color palette that compliments our logo, but designs are not limited to that palette (for example, we have found a pink (#cc1448) that compliments the palette and that we have used in the presentation).

We have also uploaded a PSD that includes icons that could compliment 9 of the 12 major selling points for the Vale Clinic Flow Platform software (the category titles are subject to change). The icons are not necessarily set in stone. For consistency with our presentation, the Protection, Integration, and Review icons should be used, but any of the remaining six (in particular, the Personalized icon) can be changed to whatever you think might be more suitable. The PSD also has some preliminary text for a few of the 12 selling points (we are refining the text now and will get the final content to designers very soon). Also note that the font is simply a placeholder; use whatever font you think would best compliment your design. Finally, keep in mind that the PSD does NOT reflect a design we are looking for; in fact, we hate this "design" and hesitate to call it a design. It was simply a way to arrange the elements to easily distribute them to designers.

We want an 8 1/2in x 11in 8-page flyer that is professional, simple, and has a clear message: this product will revolutionize your practice! We of course also need a website design that compliments the flyer design once the flyer design is finalized and chosen.

We will be monitoring this project closely-- please ask any questions you have!
Updates

Target Market(s)

Physicians, technicians, and marketing personnel in the LASIK industry.

Industry/Entity Type

Software

Number of Pages Required

4 page

Font styles to use
Serif
Sans Serif

```html
<!DOCTYPE html>
<html lang="en">
<head>
<meta charset="utf-8">
<title>Vale Clinic Flow Platform – Flyer Page</title>
<link rel="stylesheet" href="https://fonts.googleapis.com/css2?family=Cinzel:wght@400;700&display=swap">
<style>
  :root {
    --ink-black: #000000;
    --frame-white: #ffffff;
    --header-green: #178a6b;
    --corner-navy: #0c2f45;
    --panel-teal: #0e4a5d;
    --panel-teal-deep: #0b4254;
    --rail-yellow: #f2c515;
    --highlight-gold: #e3c21c;
    --rule-gold: #d8b21a;
    --icon-green: #16866a;
    --text-light: #f3f5f4;
    --serif: 'Cinzel', 'Trajan Pro', Georgia, serif;
  }
  * { box-sizing: border-box; margin: 0; padding: 0; }
  html, body {
    width: 950px; height: 1200px; overflow: hidden;
    background: var(--ink-black);
  }
  .flyer {
    position: absolute; left: 47px; top: 47px;
    width: 858px; height: 1106px;
    border: 3px solid var(--frame-white);
    border-radius: 3px;
    background: var(--panel-teal);
    overflow: hidden;
    font-family: var(--serif);
    color: var(--text-light);
  }
  .header {
    position: absolute; left: 0; top: 0; width: 100%; height: 163px;
    background: var(--header-green);
    border-bottom: 2px solid var(--rule-gold);
  }
  .header-corner { position: absolute; right: 0; top: 0; }
  .intro {
    position: absolute; left: 21px; top: 36px; width: 640px;
    font-size: 21px; line-height: 31px; letter-spacing: 0.2px;
  }
  .brand {
    position: absolute; right: 24px; top: 24px;
    display: flex; align-items: center; gap: 8px;
    font-size: 14px; font-weight: 700; color: var(--frame-white);
    letter-spacing: 0.5px;
  }
  .brand-dot {
    width: 14px; height: 14px; border-radius: 50%;
    background: var(--rail-yellow);
  }
  .rail {
    position: absolute; left: 0; top: 165px; bottom: 0; width: 76px;
    background: var(--rail-yellow);
  }
  .panel-shade {
    position: absolute; left: 76px; top: 165px; right: 0; bottom: 0;
    background: linear-gradient(180deg, var(--panel-teal) 0%, var(--panel-teal-deep) 100%);
  }
  .point-icon {
    position: absolute; left: 12px;
    width: 102px; height: 102px; border-radius: 50%;
    background: var(--frame-white);
    border: 4px solid var(--icon-green);
    box-shadow: 0 0 0 3px var(--frame-white);
    display: flex; align-items: center; justify-content: center;
  }
  .point-text {
    position: absolute; left: 143px; width: 695px;
    font-size: 16.5px; line-height: 24px;
  }
  .keyword {
    font-weight: 700; font-size: 20px; color: var(--highlight-gold);
    letter-spacing: 0.5px;
  }
  .icon-connectivity { top: 198px; }
  .text-connectivity { top: 206px; }
  .icon-personalized { top: 451px; }
  .text-personalized { top: 441px; }
  .icon-integration { top: 687px; }
  .text-integration { top: 677px; }
  .icon-protection { top: 926px; }
  .text-protection { top: 900px; }
  .web-tag {
    position: absolute; right: 4px; bottom: 4px;
    width: 264px; height: 36px;
    background: var(--header-green);
    display: flex; align-items: center; justify-content: center;
    font-size: 16px; white-space: nowrap; color: var(--frame-white);
  }
</style>
</head>
<body>
<main class="flyer">
  <header class="header">
    <svg class="header-corner" width="180" height="161" viewBox="0 0 180 161" aria-hidden="true">
      <path d="M30 0 H180 V161 H120 C130 120 110 95 80 90 C60 60 50 25 30 0 Z" fill="var(--corner-navy)"/>
      <path d="M58 161 C70 125 100 100 140 105 C160 108 175 120 180 128 V161 Z" fill="var(--header-green)"/>
    </svg>
    <div class="brand"><span class="brand-dot"></span>Copper Vale Systems</div>
    <p class="intro">Intro text here Intro text here Intro text here Intro text here Intro text here Intro text here Intro text here Intro text here Intro text here</p>
  </header>

  <div class="rail"></div>
  <div class="panel-shade"></div>

  <div class="point-icon icon-connectivity">
    <svg width="60" height="50" viewBox="0 0 60 50" aria-hidden="true">
      <path d="M4 10 H30 V2 L44 16 L30 30 V22 H4 Z" fill="var(--icon-green)"/>
      <path d="M56 28 H30 V20 L16 34 L30 48 V40 H56 Z" fill="var(--icon-green)"/>
    </svg>
  </div>
  <p class="point-text text-connectivity">It's time for a revolution in an industry that depends on effective marketing, tracking marketing campaign effectiveness, and converting interest into procedures. Finally comes the solution: the Vale Clinic Flow Platform which includes <span class="keyword">Connectivity</span> between your marketing records and your patient records. Two databases, one for patients and one for prospective patients, with a single program connecting them. It's simple, it's HIPAA-compliant, and it's only the beginning.</p>

  <div class="point-icon icon-personalized">
    <svg width="50" height="60" viewBox="0 0 50 60" fill="none" stroke="var(--icon-green)" stroke-width="2.4" stroke-linecap="round" aria-hidden="true">
      <path d="M8 22 C10 8 40 8 42 22"/>
      <path d="M12 30 C12 14 38 14 38 30 V38"/>
      <path d="M17 44 V30 C17 20 33 20 33 30 V46"/>
      <path d="M22 52 V30 C22 25 28 25 28 30 V52"/>
      <path d="M6 32 V40 M44 30 V42 M12 42 V48 M38 44 V50"/>
    </svg>
  </div>
  <p class="point-text text-personalized">Contact with prospective and current patients is key in a market of elective procedures. Communication must be efficient, standardized, but also <span class="keyword">Personalized,</span> The Vale Clinic Flow Platform does it all by incorporating the patient and contact database information in your communications. The Suite offers an array of customizable, personalized emails, texts, and even printouts for appointment reminders, surgery prepartion information, and referral programs - all with a few clicks.</p>

  <div class="point-icon icon-integration">
    <svg width="56" height="56" viewBox="0 0 56 56" aria-hidden="true">
      <rect x="4" y="4" width="22" height="22" fill="var(--icon-green)"/>
      <rect x="30" y="4" width="22" height="22" fill="var(--icon-green)"/>
      <rect x="4" y="30" width="22" height="22" fill="var(--icon-green)"/>
      <rect x="30" y="30" width="22" height="22" fill="var(--icon-green)"/>
      <circle cx="28" cy="15" r="5" fill="var(--icon-green)"/>
      <circle cx="15" cy="28" r="5" fill="var(--icon-green)"/>
      <circle cx="41" cy="28" r="5" fill="var(--icon-green)"/>
      <circle cx="28" cy="41" r="5" fill="var(--icon-green)"/>
    </svg>
  </div>
  <p class="point-text text-integration">In the digital age our industry still requires patients to fill out forms with&nbsp; pen and paper which in turn have to be entered into a database by hand. Technicians must take digital information from [device], print it out into physical paper, then enter the data back into digital format. We say, "No more." With the Vale Clinic Flow Platform your practice will enjoy full digital <span class="keyword">Integration</span> of all key equipment, including the laser, the Wavefront, and the HIPAA-compliant databases that connect them.</p>

  <div class="point-icon icon-protection">
    <svg width="60" height="60" viewBox="0 0 60 60" aria-hidden="true">
      <path d="M4 28 C6 10 54 10 56 28 C50 24 44 24 40 28 C36 24 24 24 20 28 C16 24 10 24 4 28 Z" fill="var(--icon-green)"/>
      <path d="M30 12 V48 C30 54 22 54 22 48" fill="none" stroke="var(--icon-green)" stroke-width="3" stroke-linecap="round"/>
    </svg>
  </div>
  <p class="point-text text-protection">With your key devices linked together in an integrated system, the Vale Clinic Flow Platform offers significant <span class="keyword">Protection</span> for you and your practice. In addition to streamlining operations, not having to enter data multiple times means you are protected from human errors that can lead to lawsuits.</p>

  <div class="web-tag">www.coppervale.example</div>
</main>
</body>
</html>
```